Graphic- Educational Visual

Bramble Dog Training has created an educational tool to help its students understand and prioritize some key concepts in their dog training.

We are requesting a visual of this tool be designed.

Name/title of tool (to be included in graphic): The Bramble Compass
Description: Funnel (inverted pyramid).

From top to bottom, the levels are called:

Connect
Develop
Progress
Refine

The diagram should also include a cycle around it to, to represent that one is always moving through the levels.

Business colours are included below to make sure the funnel's colours complement the website colours or at least don't clash:

#0AA1C7 Blue and #7FC31B Green
Purple as a secondary colour -75279C

For reference, business logo is attached.

```html
<!DOCTYPE html>
<html lang="en">
<head>
<meta charset="utf-8">
<title>The Bramble Compass</title>
<link rel="stylesheet" href="https://fonts.googleapis.com/css2?family=Montserrat:wght@700&family=Cabin:wght@600&display=swap">
<style>
  :root {
    --brand-blue: #1aa0c8;
    --brand-green: #80c343;
    --ribbon-dark: #404040;
    --paper: #ffffff;
    --label-ink: #ffffff;
  }
  html, body {
    margin: 0;
    padding: 0;
    overflow: hidden;
    background: var(--paper);
  }
  .canvas {
    position: relative;
    width: 1200px;
    height: 1200px;
    background: var(--paper);
    overflow: hidden;
  }
  .tool-title {
    position: absolute;
    top: 112px;
    left: 0;
    width: 1200px;
    margin: 0;
    text-align: center;
    font-family: "Montserrat", sans-serif;
    font-weight: 700;
    font-size: 72px;
    line-height: 1.05;
    letter-spacing: 0.5px;
    color: var(--brand-blue);
  }
  .funnel {
    position: absolute;
    top: 0;
    left: 0;
    width: 1200px;
    height: 1200px;
  }
  .band--blue { fill: var(--brand-blue); }
  .band--green { fill: var(--brand-green); }
  .ribbon-fold { fill: var(--ribbon-dark); }
  .level-label {
    font-family: "Cabin", sans-serif;
    font-weight: 600;
    font-size: 44px;
    fill: var(--label-ink);
  }
  .level-icon { fill: var(--label-ink); }
  .level-icon--stroke {
    fill: none;
    stroke: var(--label-ink);
    stroke-width: 5;
    stroke-linecap: round;
    stroke-linejoin: round;
  }
</style>
</head>
<body>
<main class="canvas">
  <h1 class="tool-title">The Bramble<br>Compass</h1>

  <svg class="funnel" viewBox="0 0 1200 1200" role="img" aria-label="Funnel with four levels: Connect, Develop, Progress, Refine">
    <!-- ribbon folds between levels -->
    <polygon class="ribbon-fold" points="640,531 968,531 640,626 274,626"/>
    <polygon class="ribbon-fold" points="640,721 884,721 640,816 357,816"/>
    <polygon class="ribbon-fold" points="640,910 802,910 640,1005 440,1005"/>

    <!-- level bands -->
    <polygon class="band--blue" points="192,437 1008,437 968,531 232,531"/>
    <polygon class="band--green" points="274,626 926,626 886,721 314,721"/>
    <polygon class="band--blue" points="357,816 843,816 802,910 398,910"/>
    <polygon class="band--green" points="440,1005 760,1005 720,1100 480,1100"/>

    <!-- Connect -->
    <g class="level level--connect">
      <g class="level-icon--stroke" transform="translate(520 484) rotate(-45)">
        <rect x="-24" y="-8" width="26" height="16" rx="8"/>
        <rect x="-2" y="-8" width="26" height="16" rx="8"/>
      </g>
      <text class="level-label" x="572" y="500">Connect</text>
    </g>

    <!-- Develop -->
    <g class="level level--develop">
      <path class="level-icon" d="M520,696 C500,682 497,668 497,662 C497,650 506,644 514,644 C519,644 522,647 520,650 C518,647 521,644 526,644 C534,644 543,650 543,662 C543,668 540,682 520,696 Z" transform="translate(-0 0)"/>
      <text class="level-label" x="572" y="690">Develop</text>
    </g>

    <!-- Progress -->
    <g class="level level--progress">
      <polyline class="level-icon--stroke" points="510,880 522,858 530,868 543,848"/>
      <polygon class="level-icon" points="534,846 548,842 545,856"/>
      <text class="level-label" x="572" y="880">Progress</text>
    </g>

    <!-- Refine -->
    <g class="level level--refine">
      <path class="level-icon" d="M507,1048 h10 v26 h-10 Z M520,1074 v-26 l8,-12 c2,-4 3,-10 3,-14 c4,0 8,4 7,12 l-2,10 h10 c4,0 6,3 5,6 c2,2 2,5 0,7 c2,2 1,5 -1,7 c1,3 -1,6 -5,6 Z"/>
      <text class="level-label" x="572" y="1070">Refine</text>
    </g>
  </svg>
</main>
</body>
</html>
```